HVAC Door Hanger- 4.25 inches by 11 inches

Hello We are using the Brightvale door hanger as an inspiration for our new door hanger. The company name is Corvant Home Services. Logo files attached. The Slogan needs to be added on the front with the Logo "Southern California’s Trusted Name in Home Services". Instead of the X protection plan, the name will be Full Shield by Corvant or Corvant Climate Keeper- The slogan for this package will be "Peace of Mind, For Every Season

```html
<!DOCTYPE html>
<html lang="en">
<head>
<meta charset="utf-8">
<title>Corvant Home Services – Door Hanger</title>
<link href="https://fonts.googleapis.com/css2?family=Montserrat:wght@600;700;800;900&family=Poppins:wght@500;600;700&display=swap" rel="stylesheet">
<style>
:root{
  --blue:#1f78b8;
  --blue-dark:#17629a;
  --orange:#f59a22;
  --red:#c4161c;
  --dark:#333333;
  --gold:#e7c25a;
  --white:#ffffff;
  --stage-top:#a4a4a4;
  --stage-bottom:#d1d1d1;
}
*{margin:0;padding:0;box-sizing:border-box}
html,body{width:1200px;height:3167px;overflow:hidden}
body{position:relative;background:var(--stage-bottom);font-family:'Poppins',sans-serif}
.stage-top{position:absolute;left:0;top:0;width:1200px;height:1541px;background:var(--stage-top)}
.panel{position:absolute;width:470px;height:1213px;background:var(--white);overflow:hidden}
.row-top{top:141px;--hole:var(--stage-top)}
.row-bottom{top:1737px;--hole:var(--stage-bottom)}
.side-front{left:108px}
.side-back{left:630px}
.art{position:absolute;left:0;top:0;width:470px;height:1213px}
.hole{position:absolute;left:149px;top:78px;width:172px;height:172px;border-radius:50%;background:var(--hole)}
.abs{position:absolute}
.center{left:0;width:100%;text-align:center}

/* brand block */
.brand{left:58px;top:288px;width:354px}
.brand-name{display:flex;align-items:center;gap:8px;font-family:'Montserrat',sans-serif;font-weight:800;font-size:21px;color:var(--blue);letter-spacing:.3px;white-space:nowrap}
.brand-mark{width:18px;height:18px;background:var(--orange);flex:none}
.brand-trades{margin-top:8px;font-family:'Montserrat',sans-serif;font-weight:700;font-size:11px;letter-spacing:1.4px;color:var(--red);white-space:nowrap}
.brand-tagline{margin-top:3px;text-align:right;font-family:'Montserrat',sans-serif;font-weight:600;font-size:6.5px;letter-spacing:2px;color:var(--dark)}

/* front */
.slogan-top{top:452px;font-family:'Montserrat',sans-serif;font-weight:900;font-size:39px;line-height:37px;color:var(--white)}
.slogan-pill{left:59px;top:534px;width:351px;height:37px;border-radius:19px;background:var(--red);color:var(--white);font-family:'Montserrat',sans-serif;font-weight:900;font-size:28px;line-height:37px;text-align:center}
.slogan-big{top:579px;font-family:'Montserrat',sans-serif;font-weight:900;font-size:64px;line-height:58px;color:var(--orange)}

/* back */
.plan-title{top:416px;font-family:'Montserrat',sans-serif;font-weight:900;font-size:23px;line-height:22px;color:var(--white)}
.plan-title .accent{color:var(--orange)}
.benefit{display:flex;align-items:flex-start;gap:8px;color:var(--white);font-family:'Montserrat',sans-serif;font-size:12px;font-weight:700;line-height:16px}
.benefit span{width:132px}
.benefit-icon{flex:none;width:30px;height:30px;border-radius:50%;background:var(--white);border:2px solid var(--orange);position:relative}
.benefit-icon::after{content:"";position:absolute;left:9px;top:9px;width:8px;height:8px;border-radius:2px;background:var(--blue)}
.offer-banner{left:95px;top:695px;width:322px;height:46px;background:var(--red);border-radius:8px 8px 0 0;color:var(--white);font-family:'Montserrat',sans-serif;font-weight:700;font-size:11.5px;line-height:15px;padding:9px 0 0 62px;text-align:center}
.offer-seal{left:58px;top:676px;width:64px;height:64px;border-radius:50%;background:var(--gold);border:3px solid var(--white);color:var(--dark);font-family:'Montserrat',sans-serif;font-weight:900;font-size:16px;line-height:17px;text-align:center;padding-top:12px}
.offer-box{left:52px;top:741px;width:365px;height:136px;background:var(--white);border-radius:0 0 14px 14px}
.offer-head{top:750px;font-family:'Montserrat',sans-serif;font-weight:800;font-size:15px;color:var(--red)}
.offer-item{padding-left:11px;font-size:10.5px;font-weight:500;line-height:13px;color:var(--dark)}
.offer-item::before{content:"";position:absolute;left:0;top:4px;width:6px;height:6px;border-radius:50%;background:var(--orange)}
.col-left{left:66px;width:135px}
.col-right{left:210px;width:125px}
.line-one{top:784px}
.line-two{top:820px}
.offer-price{left:341px;top:776px;width:62px;height:62px;border-radius:50%;background:var(--red);color:var(--white);font-family:'Montserrat',sans-serif;font-weight:900;text-align:center;padding-top:10px}
.offer-price small{display:block;font-size:13px;line-height:14px}
.offer-price b{display:block;font-size:24px;line-height:24px}
.offer-ribbon{left:95px;top:857px;width:277px;height:36px;background:var(--red);border-radius:4px;color:var(--white);font-family:'Montserrat',sans-serif;font-weight:800;font-size:18px;line-height:36px;text-align:center}

/* contact */
.phone-badge{left:214px;top:1028px;width:42px;height:42px;border-radius:50%;background:var(--blue);border:3px solid var(--orange)}
.phone-badge svg{position:absolute;left:9px;top:9px}
.phone-number{top:1072px;font-family:'Montserrat',sans-serif;font-weight:800;font-size:44px;color:var(--dark)}
.web-pill{left:30px;top:1137px;width:410px;height:47px;border-radius:12px;background:var(--dark);color:var(--white);font-family:'Montserrat',sans-serif;font-weight:700;font-size:21px;line-height:47px;text-align:center}
.web-pill span{color:var(--orange)}
</style>
</head>
<body>
<div class="stage-top"></div>

<!-- ===== Front, row 1 ===== -->
<section class="panel row-top side-front">
  <svg class="art" viewBox="0 0 470 1213" aria-hidden="true">
    <defs>
      <linearGradient id="unitsA" x1="0" y1="0" x2="1" y2="1"><stop offset="0" stop-color="#e6e8ea"/><stop offset="1" stop-color="#8f969c"/></linearGradient>
      <linearGradient id="fanA" x1="0" y1="0" x2="1" y2="1"><stop offset="0" stop-color="#f4f4f4"/><stop offset=".6" stop-color="#c8ccd0"/><stop offset="1" stop-color="#3a5d8f"/></linearGradient>
    </defs>
    <polygon points="0,365 123,430 0,531" fill="var(--orange)"/>
    <polygon points="470,365 347,430 470,531" fill="var(--orange)"/>
    <polygon points="235,372 470,548 470,1110 0,1110 0,548" fill="var(--blue)" stroke="var(--white)" stroke-width="6"/>
    <rect x="0" y="730" width="300" height="380" fill="url(#unitsA)" role="img" aria-label="Photo of outdoor air conditioning units"/>
    <polygon points="349,707 452,766 452,882 349,941 246,882 246,766" fill="url(#fanA)" stroke="var(--white)" stroke-width="6" role="img" aria-label="Photo of a technician checking an AC fan with gauges"/>
    <rect x="76" y="925" width="37" height="180" fill="var(--blue)"/>
    <rect x="72" y="917" width="45" height="9" rx="3" fill="var(--orange)"/>
    <polygon points="235,904 480,1090 480,1220 -10,1220 -10,1090" fill="var(--white)" stroke="var(--blue)" stroke-width="14"/>
  </svg>
  <div class="hole"></div>
  <div class="abs brand">
    <div class="brand-name"><span>CORVANT HOME SERVICES</span><i class="brand-mark"></i></div>
    <div class="brand-trades">HEATING COOLING PLUMBING ELECTRICAL</div>
    <div class="brand-tagline">• AT A PRICE YOU'LL LOVE •</div>
  </div>
  <div class="abs center slogan-top">SOUTHERN<br>CALIFORNIA’S</div>
  <div class="abs slogan-pill">TRUSTED NAME IN</div>
  <div class="abs center slogan-big">HOME<br>SERVICES</div>
  <div class="abs phone-badge"><svg width="18" height="18" viewBox="0 0 24 24"><path fill="#fff" d="M6.6 10.8a15.1 15.1 0 0 0 6.6 6.6l2.2-2.2a1 1 0 0 1 1-.25 11.4 11.4 0 0 0 3.6.57 1 1 0 0 1 1 1V20a1 1 0 0 1-1 1A17 17 0 0 1 3 4a1 1 0 0 1 1-1h3.5a1 1 0 0 1 1 1c0 1.25.2 2.45.57 3.57a1 1 0 0 1-.25 1z"/></svg></div>
  <div class="abs center phone-number">(555) 470-2188</div>
  <div class="abs web-pill">www.<span>corvanthomeservices</span>.com</div>
</section>

<!-- ===== Back, row 1 ===== -->
<section class="panel row-top side-back">
  <svg class="art" viewBox="0 0 470 1213" aria-hidden="true">
    <polygon points="0,365 123,430 0,531" fill="var(--orange)"/>
    <polygon points="470,365 347,430 470,531" fill="var(--orange)"/>
    <polygon points="235,372 470,548 470,1110 0,1110 0,548" fill="var(--blue)" stroke="var(--white)" stroke-width="6"/>
    <rect x="76" y="925" width="37" height="180" fill="var(--blue-dark)"/>
    <rect x="72" y="917" width="45" height="9" rx="3" fill="var(--orange)"/>
    <polygon points="235,904 480,1090 480,1220 -10,1220 -10,1090" fill="var(--white)" stroke="var(--blue)" stroke-width="14"/>
  </svg>
  <div class="hole"></div>
  <div class="abs brand">
    <div class="brand-name"><span>CORVANT HOME SERVICES</span><i class="brand-mark"></i></div>
    <div class="brand-trades">HEATING COOLING PLUMBING ELECTRICAL</div>
    <div class="brand-tagline">• AT A PRICE YOU'LL LOVE •</div>
  </div>
  <div class="abs center plan-title"><span class="accent">FULL SHIELD</span><br>BY<br>CORVANT</div>
  <div class="abs benefit" style="left:54px;top:508px"><i class="benefit-icon"></i><span>One X Performance Heating Tune-up per year</span></div>
  <div class="abs benefit" style="left:237px;top:508px"><i class="benefit-icon"></i><span>One X Performance A/C Tune-up per year</span></div>
  <div class="abs benefit" style="left:54px;top:576px"><i class="benefit-icon"></i><span>Transferrable Plan</span></div>
  <div class="abs benefit" style="left:237px;top:576px"><i class="benefit-icon"></i><span>One Water Heater Flush per year</span></div>
  <div class="abs benefit" style="left:54px;top:626px"><i class="benefit-icon"></i><span>10% Off In-Door Air Quality Products</span></div>
  <div class="abs benefit" style="left:237px;top:626px"><i class="benefit-icon"></i><span>Priority Installation</span></div>
  <div class="abs offer-banner">MONTHLY SERVICE REDUCED FROM<br><span style="color:var(--gold)">$29.99/MONTH</span> TO <span style="color:var(--gold)">$19.99/MONTH</span></div>
  <div class="abs offer-box"></div>
  <div class="abs offer-seal">REG.<br>$176!</div>
  <div class="abs center offer-head">PEACE OF MIND, FOR EVERY SEASON</div>
  <div class="abs offer-item col-left line-one">A/C System Safety Inspection Tune-Up</div>
  <div class="abs offer-item col-right line-one">Whole Home Water Safety Inspection</div>
  <div class="abs offer-item col-left line-two">Standard Water Heater Flush in</div>
  <div class="abs offer-item col-right line-two">Accessible Drain Cleaning</div>
  <div class="abs offer-price"><small>ONLY</small><b>$88</b></div>
  <div class="abs offer-ribbon">LIMITED TIME OFFERS!</div>
  <div class="abs phone-badge"><svg width="18" height="18" viewBox="0 0 24 24"><path fill="#fff" d="M6.6 10.8a15.1 15.1 0 0 0 6.6 6.6l2.2-2.2a1 1 0 0 1 1-.25 11.4 11.4 0 0 0 3.6.57 1 1 0 0 1 1 1V20a1 1 0 0 1-1 1A17 17 0 0 1 3 4a1 1 0 0 1 1-1h3.5a1 1 0 0 1 1 1c0 1.25.2 2.450.57 3.57a1 1 0 0 1-.25 1z"/></svg></div>
  <div class="abs center phone-number">(555) 470-2188</div>
  <div class="abs web-pill">www.<span>corvanthomeservices</span>.com</div>
</section>

<!-- ===== Front, row 2 ===== -->
<section class="panel row-bottom side-front">
  <svg class="art" viewBox="0 0 470 1213" aria-hidden="true">
    <defs>
      <linearGradient id="unitsB" x1="0" y1="0" x2="1" y2="1"><stop offset="0" stop-color="#e6e8ea"/><stop offset="1" stop-color="#8f969c"/></linearGradient>
      <linearGradient id="fanB" x1="0" y1="0" x2="1" y2="1"><stop offset="0" stop-color="#f4f4f4"/><stop offset=".6" stop-color="#c8ccd0"/><stop offset="1" stop-color="#3a5d8f"/></linearGradient>
    </defs>
    <polygon points="0,365 123,430 0,531" fill="var(--orange)"/>
    <polygon points="470,365 347,430 470,531" fill="var(--orange)"/>
    <polygon points="235,372 470,548 470,1110 0,1110 0,548" fill="var(--blue)" stroke="var(--white)" stroke-width="6"/>
    <rect x="0" y="730" width="300" height="380" fill="url(#unitsB)" role="img" aria-label="Photo of outdoor air conditioning units"/>
    <polygon points="349,707 452,766 452,882 349,941 246,882 246,766" fill="url(#fanB)" stroke="var(--white)" stroke-width="6" role="img" aria-label="Photo of a technician checking an AC fan with gauges"/>
    <rect x="76" y="925" width="37" height="180" fill="var(--blue)"/>
    <rect x="72" y="917" width="45" height="9" rx="3" fill="var(--orange)"/>
    <polygon points="235,904 480,1090 480,1220 -10,1220 -10,1090" fill="var(--white)" stroke="var(--blue)" stroke-width="14"/>
  </svg>
  <div class="hole"></div>
  <div class="abs brand">
    <div class="brand-name"><span>CORVANT HOME SERVICES</span><i class="brand-mark"></i></div>
    <div class="brand-trades">HEATING COOLING PLUMBING ELECTRICAL</div>
    <div class="brand-tagline">• AT A PRICE YOU'LL LOVE •</div>
  </div>
  <div class="abs center slogan-top">SOUTHERN<br>CALIFORNIA’S</div>
  <div class="abs slogan-pill">TRUSTED NAME IN</div>
  <div class="abs center slogan-big">HOME<br>SERVICES</div>
  <div class="abs phone-badge"><svg width="18" height="18" viewBox="0 0 24 24"><path fill="#fff" d="M6.6 10.8a15.1 15.1 0 0 0 6.6 6.6l2.2-2.2a1 1 0 0 1 1-.25 11.4 11.4 0 0 0 3.6.57 1 1 0 0 1 1 1V20a1 1 0 0 1-1 1A17 17 0 0 1 3 4a1 1 0 0 1 1-1h3.5a1 1 0 0 1 1 1c0 1.25.2 2.45.57 3.57a1 1 0 0 1-.25 1z"/></svg></div>
  <div class="abs center phone-number">(555) 470-2188</div>
  <div class="abs web-pill">www.<span>corvanthomeservices</span>.com</div>
</section>

<!-- ===== Back, row 2 ===== -->
<section class="panel row-bottom side-back">
  <svg class="art" viewBox="0 0 470 1213" aria-hidden="true">
    <polygon points="0,365 123,430 0,531" fill="var(--orange)"/>
    <polygon points="470,365 347,430 470,531" fill="var(--orange)"/>
    <polygon points="235,372 470,548 470,1110 0,1110 0,548" fill="var(--blue)" stroke="var(--white)" stroke-width="6"/>
    <rect x="76" y="925" width="37" height="180" fill="var(--blue-dark)"/>
    <rect x="72" y="917" width="45" height="9" rx="3" fill="var(--orange)"/>
    <polygon points="235,904 480,1090 480,1220 -10,1220 -10,1090" fill="var(--white)" stroke="var(--blue)" stroke-width="14"/>
  </svg>
  <div class="hole"></div>
  <div class="abs brand">
    <div class="brand-name"><span>CORVANT HOME SERVICES</span><i class="brand-mark"></i></div>
    <div class="brand-trades">HEATING COOLING PLUMBING ELECTRICAL</div>
    <div class="brand-tagline">• AT A PRICE YOU'LL LOVE •</div>
  </div>
  <div class="abs center plan-title"><span class="accent">FULL SHIELD</span><br>BY<br>CORVANT</div>
  <div class="abs benefit" style="left:54px;top:508px"><i class="benefit-icon"></i><span>One X Performance Heating Tune-up per year</span></div>
  <div class="abs benefit" style="left:237px;top:508px"><i class="benefit-icon"></i><span>One X Performance A/C Tune-up per year</span></div>
  <div class="abs benefit" style="left:54px;top:576px"><i class="benefit-icon"></i><span>Transferrable Plan</span></div>
  <div class="abs benefit" style="left:237px;top:576px"><i class="benefit-icon"></i><span>One Water Heater Flush per year</span></div>
  <div class="abs benefit" style="left:54px;top:626px"><i class="benefit-icon"></i><span>10% Off In-Door Air Quality Products</span></div>
  <div class="abs benefit" style="left:237px;top:626px"><i class="benefit-icon"></i><span>Priority Installation</span></div>
  <div class="abs offer-banner">MONTHLY SERVICE REDUCED FROM<br><span style="color:var(--gold)">$29.99/MONTH</span> TO <span style="color:var(--gold)">$19.99/MONTH</span></div>
  <div class="abs offer-box"></div>
  <div class="abs offer-seal">REG.<br>$176!</div>
  <div class="abs center offer-head">PEACE OF MIND, FOR EVERY SEASON</div>
  <div class="abs offer-item col-left line-one">A/C System Safety Inspection Tune-Up</div>
  <div class="abs offer-item col-right line-one">Whole Home Water Safety Inspection</div>
  <div class="abs offer-item col-left line-two">Standard Water Heater Flush in</div>
  <div class="abs offer-item col-right line-two">Accessible Drain Cleaning</div>
  <div class="abs offer-price"><small>ONLY</small><b>$88</b></div>
  <div class="abs offer-ribbon">LIMITED TIME OFFERS!</div>
  <div class="abs phone-badge"><svg width="18" height="18" viewBox="0 0 24 24"><path fill="#fff" d="M6.6 10.8a15.1 15.1 0 0 0 6.6 6.6l2.2-2.2a1 1 0 0 1 1-.25 11.4 11.4 0 0 0 3.6.57 1 1 0 0 1 1 1V20a1 1 0 0 1-1 1A17 17 0 0 1 3 4a1 1 0 0 1 1-1h3.5a1 1 0 0 1 1 1c0 1.25.2 2.45.57 3.57a1 1 0 0 1-.25 1z"/></svg></div>
  <div class="abs center phone-number">(555) 470-2188</div>
  <div class="abs web-pill">www.<span>corvanthomeservices</span>.com</div>
</section>
</body>
</html>
```